[Fun Project] Design A Website For A Semi Pro Soccer Team!

DESIGN ONLY! [NO CODING NEEDED]

Hey,

Thanks for looking! Are you ready to design a cool project with us?

This may be a once in a lifetime opportunity to design a website for a Semi Pro Soccer Team. Projects like this don't come along very often! This will be a lot of fun for you!

We need a fresh and exciting website design for a new soccer (or football, depending on where you are) team. You can view the existing site here: http://www.pwxdunefc.com/

You can get a sense of the team colors and whatnot from that, but the layout is a little dull. We need something more like this: http://www.mendelhollow.com.

We need something that is visual and exciting, something that will appeal to a sports fan. Ideally, we'd love to work with a designer is a fan of the game, as we think he/she would design something more appealing to the demographic.

Be sure to follow the link below and check out our video:

http://clipnest.com/user4417032/review/30582714/4c1d7a90fe

Thank you and good luck!

Target Market(s)

Soccer/football fans and those interested in becoming fans. More than likely, we're talking males 18-40, but don't want to rule out females.

Font styles to use
Sans Serif

Colors
faee3e
fbed22
eb1f27
000000
f6f6f6

Requirements
Must have
• Picture/video slider in the top left (see video)
1 home page design and 2 interior page designs
Should not have
• Cluttered
Dull
Lame
Poor Design
And for the love of all the is holy please do not submit us a theme or a template from some website. We are smarter then that and will just remove you from the project....REAL Designers, we got your back and won't even consider crappy stuff....

```html
<!DOCTYPE html>
<html lang="en">
<head>
<meta charset="utf-8">
<title>Pinewick Dune FC</title>
<link href="https://fonts.googleapis.com/css2?family=Open+Sans:wght@400;600;700;800&family=Questrial&display=swap" rel="stylesheet">
<style>
:root{
  --red:#d8322a;
  --red-dark:#b8231c;
  --red-soft:#e2675f;
  --yellow:#f7d42e;
  --yellow-bright:#fbed22;
  --black:#000;
  --ink:#111;
  --text:#444;
  --grey-panel:#ececec;
  --line:#3a3a3a;
  --white:#fff;
}
*{box-sizing:border-box;margin:0;padding:0}
html,body{width:913px;height:1200px;overflow:hidden}
body{position:relative;font-family:"Open Sans",Arial,sans-serif;background:var(--black);color:var(--text)}
.abs{position:absolute}
.stadium-bg{left:0;top:30px;width:913px;height:932px;background:linear-gradient(180deg,#8a8a8a 0%,#6d6d6d 40%,#3c3c3c 70%,#000 85%)}
.network-bar{left:0;top:0;width:913px;height:30px;background:var(--black);display:flex;align-items:center;padding-left:133px;gap:4px;color:#fff;font-size:9px}
.network-bar .label{font-weight:700;font-size:10px;margin-right:8px;letter-spacing:.3px}
.network-bar .badge{width:19px;height:19px;border-radius:50%;background:#5a5a5a}
.network-bar .badge.sq{border-radius:3px;background:#6a6a6a}
.network-bar .tail{margin-left:10px;font-weight:700;font-size:10px}
.page{left:131px;top:30px;width:651px;height:932px;background:var(--white)}
.promo{left:145px;top:65px;width:164px;height:55px;background:linear-gradient(90deg,#8e1a14,#c2271e);color:#fff;border:1px solid #6a0f0a}
.promo .p1{position:absolute;left:5px;top:6px;font-size:7.5px;font-weight:800;line-height:10px}
.promo .p2{position:absolute;left:72px;top:5px;font-size:7.5px;line-height:9px}
.promo .p3{position:absolute;left:108px;top:2px;font-size:24px;font-weight:800}
.promo .p4{position:absolute;left:5px;top:40px;font-size:8.5px;font-weight:800;white-space:nowrap}
.account{left:694px;top:68px;font-size:10px;font-weight:700;color:var(--ink)}
.search{left:594px;top:94px;width:173px;height:22px;border:1px solid #bbb;font-size:10px;color:#999;padding:4px 8px}
.search svg{position:absolute;right:4px;top:2px}
.nav{left:131px;top:125px;width:651px;height:30px;background:var(--red)}
.nav a{position:absolute;top:8px;color:#fff;font-size:10px;font-weight:700;text-decoration:none;transform:translateX(-50%);white-space:nowrap}
.nav .div{position:absolute;top:7px;width:1px;height:16px;background:rgba(255,255,255,.45)}
.club-name{left:405px;top:78px;width:100px;text-align:center;font-weight:800;font-size:14px;line-height:16px;color:var(--red)}
.slider{left:145px;top:172px;width:403px;height:250px;background:linear-gradient(160deg,#2b2f33,#1a1d20 45%,#3d5a2b 85%,#2c4220)}
.slider-caption{left:145px;top:365px;width:403px;height:57px;background:rgba(0,0,0,.78);color:#fff;padding:8px 15px}
.slider-caption h2{font-size:14px;font-weight:600}
.slider-caption p{font-size:8.5px;line-height:11px;margin-top:2px}
.slider-tabs{left:145px;top:422px;width:403px;height:25px;display:flex}
.slider-tabs span{flex:1;font-size:7.5px;padding:8px 0 0 6px;white-space:nowrap;overflow:hidden;color:var(--ink);background:var(--yellow);border-left:1px solid #c8a400}
.slider-tabs span.on{background:var(--black);color:#fff;border:0;padding-left:12px}
.side-title{font-size:14px;font-weight:700;color:var(--ink)}
.side-dot{width:18px;height:18px;border-radius:50%;background:var(--red)}
.matches{left:563px;top:203px;width:205px}
.match{position:relative;height:38px;margin-bottom:1px;background:var(--red-soft);color:#fff}
.match .mark{position:absolute;left:0;top:0;width:27px;height:38px;background:var(--yellow)}
.match .mark i{position:absolute;left:7px;top:12px;width:13px;height:13px;border-radius:50%;background:var(--red)}
.match b{position:absolute;left:34px;top:6px;font-size:9px}
.match small{position:absolute;left:34px;top:20px;font-size:8px}
.match svg{position:absolute;right:10px;top:11px}
.register{left:563px;top:357px;width:205px;height:90px;background:linear-gradient(90deg,#f2b42a,#ec6a28 70%,#e23a26);color:#fff;padding:10px 9px}
.register h3{font-size:18px;font-weight:700;letter-spacing:.3px}
.register p{font-size:9px;line-height:12px;margin-top:2px;width:150px}
.register svg{position:absolute;right:8px;top:28px}
.welcome{left:146px;top:462px;width:390px}
.welcome h1{font-size:19px;font-weight:700;color:var(--ink)}
.welcome p{font-size:9px;line-height:12.6px;margin-top:6px;color:#555}
.more{font-size:9.5px;color:var(--red);text-decoration:underline}
.more::after{content:" \00BB";text-decoration:none}
.news-box{left:146px;width:387px;height:156px;background:var(--grey-panel);border:1px solid #ddd}
.news-box .head{position:absolute;left:0;top:2px;width:323px;height:24px;background:var(--red);color:#fff;font-size:12.5px;font-weight:600;padding:3px 9px}
.news-box .tab{position:absolute;left:323px;top:2px;width:77px;height:24px;background:#222;color:#fff;font-size:9.5px;font-weight:600;padding:6px 0 0 11px}
.news-box .fold{position:absolute;left:387px;top:26px;width:0;height:0;border-top:13px solid #111;border-left:13px solid transparent}
.news-item{position:absolute;top:42px;width:109px}
.news-item .thumb{height:48px}
.news-item b{display:block;font-size:8px;color:var(--ink);margin-top:6px}
.news-item p{font-size:7.8px;line-height:11px;color:#555}
.weather{left:563px;top:496px;width:204px;height:144px;border:1px solid #bcd3ee;font-family:"Questrial",Arial,sans-serif;color:#555}
.weather .city{position:absolute;left:73px;top:7px;font-size:16px;color:#556}
.weather .sub{position:absolute;left:74px;top:26px;font-size:9px;color:#888}
.weather .det{position:absolute;left:74px;top:40px;font-size:7.5px;line-height:9px}
.weather .ext{position:absolute;left:16px;top:66px;font-size:8px;color:#999}
.weather .rule{position:absolute;left:16px;top:76px;width:172px;height:1px;background:#c9d6e6}
.weather .day{position:absolute;top:82px;width:40px;text-align:center;font-size:7.5px}
.weather .day svg{display:block;margin:6px auto 4px}
.wlinks{left:565px;top:648px;width:202px;font-family:"Questrial",Arial,sans-serif;font-size:7.5px}
.wlinks .l{color:#334;text-decoration:underline}
.wlinks .r{position:absolute;right:0;color:#7a8fb0;text-decoration:underline}
.player-photo{left:563px;top:728px;width:204px;height:123px;background:linear-gradient(135deg,#6b6f5a,#9a9c86 50%,#d9d9d4)}
.player-text{left:568px;top:863px;width:195px;font-size:9.5px;line-height:12.5px;color:var(--ink)}
.footer-line{left:0;top:962px;width:913px;height:8px;background:var(--yellow)}
.footer{left:0;top:970px;width:913px;height:230px;background:var(--black);color:#fff}
.fcol{position:absolute;top:22px;width:110px}
.fcol h4{font-size:11.5px;font-weight:600;color:var(--yellow-bright);margin-bottom:8px}
.fcol ul{list-style:none}
.fcol li{font-size:9px;height:18.8px;padding:3px 0 0 10px;border-bottom:1px solid var(--line);position:relative;white-space:nowrap}
.fcol li::before{content:"\00BB";position:absolute;left:2px;top:2px;color:var(--yellow);font-size:8px}
.subscribe{left:597px;top:992px;width:185px}
.subscribe h4{font-size:11.5px;font-weight:600;color:var(--yellow-bright)}
.subscribe p{font-size:8px;line-height:11px;color:#999;margin:6px 0 0 2px}
.email{left:595px;top:1044px;width:187px;height:24px;background:linear-gradient(#fff,#e6e6e6);font-size:8px;color:#999;padding:6px 9px}
.submit{left:725px;top:1079px;width:57px;height:21px;background:linear-gradient(#e9463b,#c5251d);color:#fff;font-size:9.5px;font-weight:700;text-align:center;padding-top:4px}
.social{left:455px;top:1105px}
.social h4{font-size:11.5px;font-weight:600;color:var(--yellow-bright)}
.social .dots{display:flex;gap:8px;margin-top:12px;padding-left:3px}
.social .dots i{width:11px;height:11px;border-radius:50%;background:var(--red)}
.copyright{left:650px;top:1134px;font-size:8px;color:#999}
</style>
</head>
<body>
<div class="abs stadium-bg" role="img" aria-label="Faded black and white stadium crowd and pitch"></div>

<div class="abs network-bar">
  <span class="label">NSL Network</span>
  <i class="badge"></i><i class="badge sq"></i><i class="badge"></i><i class="badge sq"></i><i class="badge"></i><i class="badge sq"></i><i class="badge"></i><i class="badge sq"></i><i class="badge"></i><i class="badge sq"></i><i class="badge"></i><i class="badge sq"></i><i class="badge"></i><i class="badge sq"></i><i class="badge"></i><i class="badge sq"></i><i class="badge"></i><i class="badge sq"></i><i class="badge"></i><i class="badge sq"></i><i class="badge"></i><i class="badge sq"></i><i class="badge"></i><i class="badge sq"></i><i class="badge"></i><i class="badge sq"></i>
  <span class="tail">NWK BRY</span>
</div>

<div class="abs page"></div>

<svg class="abs" style="left:131px;top:30px" width="651" height="40" viewBox="0 0 651 40">
  <path d="M0 0 H651 V12 C520 6 400 10 325 34 C250 10 130 6 0 12Z" fill="#f7d42e"/>
  <path d="M0 0 H651 V6 C520 2 400 4 325 22 C250 4 130 2 0 6Z" fill="#e23a26"/>
</svg>

<div class="abs promo">
  <div class="p1">CLEARBROOK<br>FAMILY<br>PACK</div>
  <div class="p2">4 Tickets<br>Meals<br>Drinks</div>
  <div class="p3">$59</div>
  <div class="p4">v. RIVERTON • SAT • 4/19 • 4PM</div>
</div>

<div class="abs account">Login &nbsp;| Register</div>
<div class="abs search">Search
  <svg width="16" height="16" viewBox="0 0 16 16"><circle cx="6.5" cy="6.5" r="5" fill="none" stroke="#222" stroke-width="2"/><path d="M10 10 L15 15" stroke="#222" stroke-width="2.4"/></svg>
</div>

<nav class="abs nav">
  <a style="left:42px">Home</a><i class="div" style="left:73px"></i>
  <a style="left:104px">News</a><i class="div" style="left:135px"></i>
  <a style="left:163px">Stats</a><i class="div" style="left:193px"></i>
  <a style="left:226px">About Us</a>
  <a style="left:403px">Tickets</a><i class="div" style="left:431px"></i>
  <a style="left:462px">Contact</a><i class="div" style="left:493px"></i>
  <a style="left:530px">Team Shop</a><i class="div" style="left:567px"></i>
  <a style="left:598px">The UDL</a>
</nav>

<div class="abs club-name">PINEWICK<br>DUNE FC</div>

<div class="abs slider" role="img" aria-label="Match action photo of players contesting the ball on a floodlit pitch"></div>
<div class="abs slider-caption">
  <h2>Ut pellentesque lorem porttitor</h2>
  <p>Aliquam nec dui ornare, mollis elit id, pulvinar mi. Phasellus facilisis lectus at fermentum faucibus.</p>
</div>
<div class="abs slider-tabs">
  <span class="on">Ut pellentesque lorem</span>
  <span>Phasellus facilisis lectus at ferm</span>
  <span>Donec ut gravida ipsum mattis</span>
</div>

<svg class="abs" style="left:565px;top:177px" width="14" height="14" viewBox="0 0 14 14"><rect x="1" y="2" width="12" height="11" fill="none" stroke="#d8322a" stroke-width="1.5"/><rect x="1" y="2" width="12" height="3" fill="#d8322a"/><path d="M4 0v4M10 0v4" stroke="#d8322a" stroke-width="1.5"/></svg>
<div class="abs side-title" style="left:586px;top:176px">Upcoming Matches</div>

<div class="abs matches">
  <div class="match"><span class="mark"><i></i></span><b>Donec ultricies felis mauris</b><small>16 May, 2014 &nbsp;| &nbsp;9:30 a.m &nbsp;| &nbsp;Kick off!</small><svg width="10" height="16"><path d="M2 1 L8 8 L2 15" fill="none" stroke="#fff" stroke-width="2.2"/></svg></div>
  <div class="match"><span class="mark"><i></i></span><b>Donec ultricies felis mauris</b><small>16 May, 2014 &nbsp;| &nbsp;9:30 a.m &nbsp;| &nbsp;Kick off!</small><svg width="10" height="16"><path d="M2 1 L8 8 L2 15" fill="none" stroke="#fff" stroke-width="2.2"/></svg></div>
  <div class="match"><span class="mark"><i></i></span><b>Donec ultricies felis mauris</b><small>16 May, 2014 &nbsp;| &nbsp;9:30 a.m &nbsp;| &nbsp;Kick off!</small><svg width="10" height="16"><path d="M2 1 L8 8 L2 15" fill="none" stroke="#fff" stroke-width="2.2"/></svg></div>
  <div class="match"><span class="mark"><i></i></span><b>Donec ultricies felis mauris</b><small>16 May, 2014 &nbsp;| &nbsp;9:30 a.m &nbsp;| &nbsp;Kick off!</small><svg width="10" height="16"><path d="M2 1 L8 8 L2 15" fill="none" stroke="#fff" stroke-width="2.2"/></svg></div>
</div>

<div class="abs register">
  <h3>2014 &nbsp;Registration</h3>
  <p>vel ultricies sem suscipit eu. Praesent a tempus velit. Praesent dignissim</p>
  <svg width="16" height="34"><path d="M2 2 L14 17 L2 32" fill="none" stroke="#fff" stroke-width="3"/></svg>
</div>

<section class="abs welcome">
  <h1>Welcome to Pinewick Dune</h1>
  <p>UDL Soccer is coming to Pinewick! The UDL is the top developmental men's league in North America. The 2013 UDL featured 64 teams within four conferences throughout the United States and Canada. The UDL season consists of 14 regular season matches for each team, seven home and seven away, and provides elite collegiate players the opportunity to taste a higher level of competition while maintaining their eligibility. In addition to league play, UDL teams compete in the Harlan Bright Open Cup as well as various...</p>
</section>
<div class="abs more" style="left:490px;top:576px">View more</div>

<section class="abs news-box" style="top:601px">
  <div class="head">Hollow Audio &amp; Notes</div><div class="tab">View more</div><i class="fold"></i>
  <div class="news-item" style="left:11px"><div class="thumb" role="img" aria-label="Players competing for a header" style="background:linear-gradient(180deg,#2d3f7a,#4b6a3a)"></div><b>Praesent vitae eleifend sap</b><p>ien, nec suscipit arcuDon ec ac nunc sed arcu rutrum gra vida. Interdum et malesuad</p></div>
  <div class="news-item" style="left:138px"><div class="thumb" role="img" aria-label="Player in white kit running with the ball" style="background:linear-gradient(180deg,#b8643a,#d59a6a)"></div><b>Praesent vitae eleifend sap</b><p>ien, nec suscipit arcuDon ec ac nunc sed arcu rutrum gra vida. Interdum et malesuad</p></div>
  <div class="news-item" style="left:263px"><div class="thumb" role="img" aria-label="Smiling fans in the stands" style="background:linear-gradient(180deg,#c9a07a,#e4b98f)"></div><b>Praesent vitae eleifend sap</b><p>ien, nec suscipit arcuDon ec ac nunc sed arcu rutrum gra vida. Interdum et malesuad</p></div>
</section>

<section class="abs news-box" style="top:773px">
  <div class="head">More Hollow News</div><div class="tab">View more</div><i class="fold"></i>
  <div class="news-item" style="left:11px"><div class="thumb" role="img" aria-label="Two players celebrating together" style="background:linear-gradient(180deg,#4e6b3a,#9a8a6a)"></div><b>Praesent vitae eleifend sap</b><p>ien, nec suscipit arcuDon ec ac nunc sed arcu rutrum gra vida. Interdum et malesuad</p></div>
  <div class="news-item" style="left:138px"><div class="thumb" role="img" aria-label="Team lined up for a photo on the pitch" style="background:linear-gradient(180deg,#3a3a3a,#7a3a30 55%,#3f7a3a)"></div><b>Praesent vitae eleifend sap</b><p>ien, nec suscipit arcuDon ec ac nunc sed arcu rutrum gra vida. Interdum et malesuad</p></div>
  <div class="news-item" style="left:263px"><div class="thumb" role="img" aria-label="Supporter cheering in the crowd" style="background:linear-gradient(180deg,#8a2a2a,#c76a5a)"></div><b>Praesent vitae eleifend sap</b><p>ien, nec suscipit arcuDon ec ac nunc sed arcu rutrum gra vida. Interdum et malesuad</p></div>
</section>

<i class="abs side-dot" style="left:566px;top:468px"></i>
<div class="abs side-title" style="left:592px;top:466px">Weather Forcast</div>

<section class="abs weather">
  <svg style="position:absolute;left:12px;top:10px" width="52" height="42" viewBox="0 0 52 42"><g stroke="#556" stroke-width="2"><path d="M30 2v5M42 8l-4 4M20 8l4 4M46 20h-5"/></g><path d="M8 36 a9 9 0 0 1 4 -17 a13 13 0 0 1 25 2 a8 8 0 0 1 0 15Z" fill="#556"/></svg>
  <div class="city">Oklahoma City</div>
  <div class="sub">Chance of Shower</div>
  <div class="det">Precipitation: 75%<br>Wind: 20 km/h</div>
  <div class="ext">Extended Forecast</div><i class="rule"></i>
  <div class="day" style="left:6px">Mon<svg width="24" height="24" viewBox="0 0 24 24"><circle cx="12" cy="12" r="6" fill="none" stroke="#556" stroke-width="2"/><g stroke="#556" stroke-width="2"><path d="M12 0v3M12 21v3M0 12h3M21 12h3M3.5 3.5l2 2M18.5 18.5l2 2M3.5 20.5l2-2M18.5 5.5l2-2"/></g></svg>21° 6°</div>
  <div class="day" style="left:56px">Tue<svg width="28" height="24" viewBox="0 0 28 24"><circle cx="15" cy="9" r="5" fill="none" stroke="#556" stroke-width="2"/><path d="M4 22 a5 5 0 0 1 3 -9 a7 7 0 0 1 13 1 a4 4 0 0 1 0 8Z" fill="#fff" stroke="#556" stroke-width="2"/></svg>19° 7°</div>
  <div class="day" style="left:106px">Wed<svg width="28" height="24" viewBox="0 0 28 24"><g stroke="#556" stroke-width="2"><path d="M15 0v3M24 9h3M22 3l-2 2"/></g><path d="M4 22 a5 5 0 0 1 3 -9 a7 7 0 0 1 13 1 a4 4 0 0 1 0 8Z" fill="#556"/></svg>21° 6°</div>
  <div class="day" style="left:156px">Thu<svg width="24" height="24" viewBox="0 0 24 24"><circle cx="12" cy="12" r="6" fill="none" stroke="#556" stroke-width="2"/><g stroke="#556" stroke-width="2"><path d="M12 0v3M12 21v3M0 12h3M21 12h3M3.5 3.5l2 2M18.5 18.5l2 2M3.5 20.5l2-2M18.5 5.5l2-2"/></g></svg>25° 10°</div>
</section>
<div class="abs wlinks"><span class="l">View Full Forecast ▸</span><span class="r">Change Location</span></div>

<i class="abs side-dot" style="left:566px;top:697px"></i>
<div class="abs side-title" style="left:592px;top:695px">This Week Featured Player</div>
<div class="abs player-photo" role="img" aria-label="Featured player in a white kit striking the ball"></div>
<p class="abs player-text">Mauris ullamcorper nunc sit amet ornare porttitor. Pellentesque varius tempor lectus dictum rutrum.</p>
<div class="abs more" style="left:712px;top:909px">View more</div>

<div class="abs footer-line"></div>
<footer class="abs footer">
  <div class="fcol" style="left:132px"><h4>&nbsp;Site map</h4><ul><li>Home</li><li>News</li><li>Stats</li><li>About</li><li>Tickets</li><li>Contact</li><li>Team Shop</li><li>The UDL</li></ul></div>
  <div class="fcol" style="left:292px"><h4>&nbsp;Quick Links</h4><ul><li>Ut pellentesque lorem</li><li>porttitor justo</li><li>fermentum, et iaculis</li><li>orci tempus. Donec</li><li>orci leo, hendrerit ut</li><li>vulputate at, iaculis sit</li><li>amet leo. Aliquam nec</li><li>dui ornare, mollis elit</li></ul></div>
  <div class="fcol" style="left:452px"><h4>&nbsp;Legal</h4><ul><li>Ut pellentesque lorem</li><li>porttitor justo</li><li>fermentum, et iaculis</li><li>orci tempus. Donec</li></ul></div>
</footer>
<div class="abs subscribe"><h4>Subscribe Newsletter</h4><p>Curabitur tempor posuere fermentum. Sed vehicula ultricies urna scelerisque fermentum</p></div>
<div class="abs email">Enter email address</div>
<div class="abs submit">Submit</div>
<div class="abs social"><h4>Get social</h4><div class="dots"><i></i><i></i><i></i><i></i></div></div>
<div class="abs copyright">Copyright 2014 All rights reserved</div>
</body>
</html>
```